Salt, Silence and Sunrise Redesign

I am looking for a redesign on my book cover. I would like to keep the same title, subtitle and author name. This book is for women between the ages of 45 - 55 that are also dealing with health and hormone issues. So if there's a photo used of a woman, it should reflect that age group and a look of frustration or hopelessness. I would also like a notation that I am a best selling author and second edition. I have attached the current book cover and a copy of my business logo. Perhaps some consistency with my business logo would be a good idea and not necessary.
I have also attached an updated back cover with an edit in text and a new picture.
If it's helpful, I am a natural doctor known as a Traditional Naturopath and my primary focus of business is helping women overcome menopause symptoms.
Note, I do not want the use of any medical pictures, such as a stethoscope or a doctor in a white coat.
I am looking for different look and theme from my current cover. Something that is a bit more luxurious or upscale from my past cover.

```html
<!DOCTYPE html>
<html lang="en">
<head>
<meta charset="utf-8">
<title>Salt, Silence and Sunrise — Second Edition Cover Wrap</title>
<link rel="stylesheet" href="https://fonts.googleapis.com/css2?family=Cormorant+Garamond:ital,wght@0,500;0,600;1,500&family=EB+Garamond:wght@400;500&family=Playfair+Display:ital,wght@0,700;1,400&display=swap">
<style>
  :root {
    --backdrop: #a5a19e;
    --paper: #f8f5f7;
    --spine: #ffffff;
    --plum-deep: #3b0a1a;
    --plum: #6a1530;
    --wine: #8f2241;
    --rose-glow: #c9677a;
    --gold: #d9b872;
    --gold-soft: #ecd9a8;
    --ink: #1d1b1c;
    --brand: #6f8f4a;
  }
  * { box-sizing: border-box; margin: 0; padding: 0; }
  html, body { width: 1200px; height: 1200px; overflow: hidden; }
  body { background: var(--backdrop); position: relative; }

  /* Back cover */
  .back-cover {
    position: absolute; left: 33px; top: 283px; width: 484px; height: 677px;
    background: var(--paper); overflow: hidden;
  }
  .back-copy {
    position: absolute; left: 50px; top: 88px; width: 366px;
    font-family: "EB Garamond", serif; font-size: 12.6px; line-height: 16.7px;
    color: var(--ink);
  }
  .back-copy p + p { margin-top: 16.7px; }
  .brand-mark {
    position: absolute; left: 51px; top: 444px;
    display: flex; align-items: center; gap: 9px;
  }
  .brand-dot { width: 18px; height: 18px; border-radius: 50%; background: var(--brand); }
  .brand-name {
    font-family: "EB Garamond", serif; font-weight: 500; font-size: 22px;
    color: var(--brand);
  }
  .author-photo {
    position: absolute; left: 290px; top: 482px; width: 172px; height: 195px;
    border-radius: 86px 86px 0 0;
    background: linear-gradient(180deg, #d8c2b4 0%, #c9a792 40%, #b9a3cc 75%, #a995c2 100%);
  }

  .spine {
    position: absolute; left: 572px; top: 283px; width: 53px; height: 675px;
    background: var(--spine);
  }

  /* Front cover */
  .front-cover {
    position: absolute; left: 685px; top: 280px; width: 476px; height: 673px;
    background:
      radial-gradient(ellipse 70% 45% at 50% 62%, rgba(201,103,122,0.55) 0%, rgba(143,34,65,0) 70%),
      linear-gradient(160deg, var(--plum-deep) 0%, var(--plum) 48%, var(--wine) 100%);
    overflow: hidden; text-align: center; color: var(--gold-soft);
  }
  .cover-frame {
    position: absolute; inset: 12px; border: 1px solid var(--gold); pointer-events: none;
  }
  .edition-label {
    position: absolute; left: 0; right: 0; top: 30px;
    font-family: "Cormorant Garamond", serif; font-weight: 600; font-size: 13px;
    letter-spacing: 5px; text-transform: uppercase; color: var(--gold);
  }
  .front-title {
    position: absolute; left: 0; right: 0; top: 56px;
    font-family: "Playfair Display", serif; font-weight: 700; line-height: 1;
    color: var(--gold-soft);
  }
  .title-top { display: block; font-size: 42px; letter-spacing: 2px; text-transform: uppercase; }
  .title-and { display: block; font-family: "Playfair Display", serif; font-style: italic; font-weight: 400; font-size: 26px; margin-top: 6px; color: var(--gold); }
  .title-bottom { display: block; font-size: 60px; letter-spacing: 4px; text-transform: uppercase; margin-top: 4px; }
  .title-rule {
    position: absolute; left: 188px; top: 210px; width: 100px; height: 1px; background: var(--gold);
  }
  .front-subtitle {
    position: absolute; left: 0; right: 0; top: 224px;
    font-family: "Cormorant Garamond", serif; font-style: italic; font-weight: 500;
    font-size: 21px; line-height: 24px; color: var(--gold-soft);
  }
  .cover-photo {
    position: absolute; left: 138px; top: 290px; width: 200px; height: 262px;
    border-radius: 100px 100px 0 0; border: 1px solid var(--gold);
    background: linear-gradient(180deg, #b58a7a 0%, #8e5a5e 55%, #5a2236 100%);
  }
  .bestseller-label {
    position: absolute; left: 0; right: 0; top: 570px;
    font-family: "Cormorant Garamond", serif; font-weight: 600; font-size: 13px;
    letter-spacing: 4px; text-transform: uppercase; color: var(--gold);
  }
  .front-author {
    position: absolute; left: 0; right: 0; top: 592px;
    font-family: "Cormorant Garamond", serif; font-weight: 600; font-size: 24px;
    letter-spacing: 1px; line-height: 1; color: var(--gold-soft);
  }
  .front-foreword {
    position: absolute; left: 0; right: 0; top: 626px;
    font-family: "Cormorant Garamond", serif; font-style: italic; font-weight: 500;
    font-size: 16px; color: var(--gold);
  }
</style>
</head>
<body>
  <section class="back-cover">
    <div class="back-copy">
      <p>Imagine how good it feels when you are able to easily slip into your sexy skinny jeans, have energy all day and feel truly happy. “Salt, Silence and Sunrise?” provides proven and effective secrets that give you the ability to achieve this all the while getting your life back on many levels.</p>
      <p>It’s a book that explains the how and why you became overweight, fatigued and frustrated in the first place. It outlines simple, effective, and proven strategies in a step by step way that will have you slipping on your skinny jeans, enjoying abundant energy and returning to your happy self again. Yes, you can reverse the clock! orem ipsum dolor sit amet, consectetur adipiscing elit, sed do eiusmod tempor incididunt ut labore et dolore magna aliqua. Quis ipsum suspendisse ultrices gravida. Risus commodo viverra maecenas accumsan lacus vel facilisis.</p>
      <p>Traditional Naturopath, Owen Hartley was able to overcome epilepsy naturally and in the process a passion erupted inside of him to help people heal “incurable” health diseases. Since then Owen has stayed at the forefront of Natural Medicine by working alongside leaders in the field, most notably Dr. Samuel Brandt. This book is a result of his research, experience, and the learnings from helping thousands of people, just like</p>
    </div>
    <div class="brand-mark">
      <span class="brand-dot"></span>
      <span class="brand-name">Hartley Wellness</span>
    </div>
    <div class="author-photo" role="img" aria-label="Portrait photo of the smiling author in a lavender shirt"></div>
  </section>

  <div class="spine"></div>

  <section class="front-cover">
    <div class="cover-frame"></div>
    <p class="edition-label">Second Edition</p>
    <h1 class="front-title">
      <span class="title-top">Salt, Silence</span>
      <span class="title-and">and</span>
      <span class="title-bottom">Sunrise</span>
    </h1>
    <div class="title-rule"></div>
    <p class="front-subtitle">how to reverse the clock<br>and feel young again</p>
    <div class="cover-photo" role="img" aria-label="Photo of a woman in her late forties, looking weary and frustrated, in soft warm light"></div>
    <p class="bestseller-label">Best-Selling Author</p>
    <p class="front-author">Owen Hartley | Traditional Naturopath</p>
    <p class="front-foreword">Forward by Dr. Martin Ellery</p>
  </section>
</body>
</html>
```